Business Card Design

building company specialistloft conversion,extension ,bathrooms ,kitchens ,painting and decorating all general building work

Industry/Entity Type

Building

Contact Information for Business Card

K&M Property renovation Ltd
tel -07914638205
email-Mdorin07@brixmail.net
web in progres

Font styles to use
Sans Serif

Requirements
Must have
• name of the company
• all contact details
Nice to have
• some of the skills

```html
<!DOCTYPE html>
<html lang="en">
<head>
<meta charset="utf-8">
<title>K&amp;M Property renovation Ltd – Business Card</title>
<link rel="stylesheet" href="https://fonts.googleapis.com/css2?family=Kumbh+Sans:wght@500;600&display=swap">
<style>
  :root {
    --paper: #ffffff;
    --card-dark: #1d1f1f;
    --accent-red: #ff2a00;
    --accent-orange: #ff5300;
    --text-light: #ffffff;
    --text-soft: #d9d9d9;
    --trim-line: #1a1a1a;
    --safe-line: #e0403a;
  }
  html, body {
    margin: 0;
    padding: 0;
    width: 1200px;
    height: 792px;
    overflow: hidden;
    background: var(--paper);
  }
  .card {
    position: relative;
    width: 1200px;
    height: 792px;
    background: var(--paper);
    font-family: "Kumbh Sans", sans-serif;
  }
  .guides {
    position: absolute;
    inset: 0;
  }
  .face {
    position: absolute;
    left: 48px;
    top: 48px;
    width: 1104px;
    height: 595px;
    background: var(--card-dark);
  }
  .company-name {
    position: absolute;
    left: 0;
    right: 0;
    top: 268px;
    margin: 0;
    text-align: center;
    color: var(--text-light);
    font-weight: 600;
    font-size: 44px;
    line-height: 56px;
    letter-spacing: 0.2px;
  }
  .contact {
    position: absolute;
    left: 0;
    right: 0;
    top: 348px;
    margin: 0;
    padding: 0;
    list-style: none;
    display: flex;
    justify-content: center;
    gap: 36px;
    color: var(--text-soft);
    font-weight: 500;
    font-size: 22px;
    line-height: 30px;
  }
  .contact-item {
    display: flex;
    align-items: center;
    gap: 10px;
  }
  .contact-icon {
    width: 20px;
    height: 20px;
    flex: none;
  }
  .accent-stripe {
    position: absolute;
    left: 48px;
    top: 643px;
    width: 1104px;
    height: 9px;
    background: var(--accent-red);
  }
  .services-band {
    position: absolute;
    left: 48px;
    top: 652px;
    width: 1104px;
    height: 91px;
    background: var(--accent-orange);
    display: flex;
    align-items: center;
    justify-content: center;
  }
  .services {
    margin: 0;
    margin-top: -6px;
    color: var(--text-light);
    font-weight: 600;
    font-size: 31px;
    white-space: nowrap;
  }
  .services .divider {
    display: inline-block;
    width: 4px;
    height: 28px;
    margin: 0 8px;
    background: var(--card-dark);
    vertical-align: -4px;
  }
</style>
</head>
<body>
  <div class="card">
    <svg class="guides" width="1200" height="792" viewBox="0 0 1200 792" aria-hidden="true">
      <rect x="24.5" y="24.5" width="1151" height="743" fill="none" stroke="var(--trim-line)" stroke-width="1"/>
      <rect x="26.5" y="25.5" width="1147" height="740" fill="none" stroke="var(--safe-line)" stroke-width="1"/>
    </svg>
    <div class="face">
      <h1 class="company-name">K&amp;M Property renovation Ltd</h1>
      <ul class="contact">
        <li class="contact-item">
          <svg class="contact-icon" viewBox="0 0 24 24" aria-hidden="true"><path fill="var(--accent-orange)" d="M6.6 10.8a15.1 15.1 0 0 0 6.6 6.6l2.2-2.2a1 1 0 0 1 1-.25 11.4 11.4 0 0 0 3.6.57 1 1 0 0 1 1 1V20a1 1 0 0 1-1 1A17 17 0 0 1 3 4a1 1 0 0 1 1-1h3.5a1 1 0 0 1 1 1c0 1.25.2 2.45.57 3.57a1 1 0 0 1-.25 1z"/></svg>
          <span>tel 07914638205</span>
        </li>
        <li class="contact-item">
          <svg class="contact-icon" viewBox="0 0 24 24" aria-hidden="true"><path fill="var(--accent-orange)" d="M3 5h18a1 1 0 0 1 1 1v12a1 1 0 0 1-1 1H3a1 1 0 0 1-1-1V6a1 1 0 0 1 1-1zm9 7.2L4 7.3V8l8 5 8-5v-.7z"/></svg>
          <span>Mdorin07@brixmail.net</span>
        </li>
      </ul>
    </div>
    <div class="accent-stripe"></div>
    <div class="services-band">
      <p class="services">building company specialist<span class="divider"></span>loft conversion <span class="divider"></span>all general building work</p>
    </div>
  </div>
</body>
</html>
```